Rising Paths Web Design

I am starting a new company that will provide LIFE COACHING services - I have tried to design a website, but it's too complicated. Right now, it's just me - I'm the only person that will provide services through the website - I have used artmarket to purchase a logo (see below). I want to be able to update the website myself, but need a template - basic design. Because I am not technologically savvy enough to explain in words - I basically want to have a website that will provide basic information about my services (coaching), a page about me and my background, hopefully scheduling possibilities, and testimonials — also a page for writing/blogs. I bought a website through NetHarbor - so when I have a template, I guess I”d use that - but maybe I’ll need to work with a designer to actually get it up on the internet. I have a head shot that I’ll upload, too.
Target Market(s)
Clients from the independent (private school) world - teachers, administrators
Number of Pages Required
4 page
Look and feel
Each slider illustrates characteristics of the customer's brand and the style your logo design should communicate.

```html
<!DOCTYPE html>
<html lang="en">
<head>
<meta charset="utf-8">
<title>Rising Paths Coaching</title>
<link href="https://fonts.googleapis.com/css2?family=Barlow:wght@300;400;500;600;700&family=Mulish:wght@400;600;700;800&display=swap" rel="stylesheet">
<style>
:root{
  --teal:#14a88e;
  --teal-soft:#e6f6f2;
  --ink:#2f2f31;
  --dark:#3a3a3c;
  --footer:#414042;
  --muted:#555;
  --white:#fff;
}
*{margin:0;padding:0;box-sizing:border-box}
html,body{width:1200px;height:3281px;overflow:hidden}
body{position:relative;background:var(--white);font-family:"Mulish",sans-serif;color:var(--ink)}
.abs{position:absolute}
.heading{font-family:"Barlow",sans-serif}
.nav a{position:absolute;top:72px;font-size:14.5px;color:#444;text-decoration:none;letter-spacing:.2px}
.nav a.active{color:var(--teal)}
.call{top:30px;left:825px;font-size:13px;color:#555;display:flex;align-items:center;gap:8px}
.call b{font-size:16px;color:var(--ink);font-weight:800}
.header-line{top:128px;left:660px;width:540px;height:1.5px;background:var(--teal)}
.logo{display:flex;align-items:center;justify-content:center;border-radius:50%;background:var(--white)}
.logo span{font-family:"Barlow",sans-serif;font-weight:500;color:var(--teal);letter-spacing:1px}
.logo-head{left:488px;top:-8px;width:236px;height:206px;border-radius:0 0 118px 118px;z-index:2}
.logo-ring{position:absolute;left:20px;top:18px;width:196px;height:166px;border:2px solid var(--teal);border-radius:50%}
.hero-photo{top:129px;left:0;width:600px;height:468px;background:linear-gradient(135deg,#b5624a 0%,#8b5a45 35%,#3a3236 60%,#c28d55 100%)}
.hero-bg{top:129px;left:600px;width:600px;height:468px;background:var(--teal-soft)}
.hero-title{left:682px;top:222px;font-size:51px;line-height:60px;font-weight:300;color:var(--ink)}
.hero-title strong{color:var(--teal);font-weight:600;display:block}
.hero-text{left:682px;top:352px;width:390px;font-family:"Barlow",sans-serif;font-size:18.5px;line-height:27px;color:#333}
.btn{display:flex;align-items:center;justify-content:center;background:var(--dark);color:var(--white);font-weight:800;font-size:14px;letter-spacing:.3px;border-radius:22px}
.btn-hero{left:682px;top:459px;width:277px;height:38px;border-radius:2px 20px 20px 20px}
.card{position:absolute}
.card svg{position:absolute;left:0;top:0}
.service h3{position:absolute;left:0;width:100%;top:58px;text-align:center;font-family:"Barlow",sans-serif;font-weight:500;font-size:25px;color:var(--white)}
.service p{position:absolute;left:22px;right:22px;top:100px;text-align:center;font-size:13px;line-height:21px;color:var(--white)}
.service .arrow{position:absolute;left:152px;top:186px}
.about-title{left:172px;top:1040px;font-size:41px;line-height:50px;font-weight:400}
.about-title strong{display:block;color:var(--teal);font-weight:600}
.about-text{left:172px;top:1162px;width:450px;font-size:13.3px;line-height:19.5px;color:#333}
.about-text p{margin-bottom:19px}
.signature{left:172px;top:1328px;width:210px;height:56px;background:linear-gradient(90deg,#e9e9e9,#f5f5f5);border-radius:6px}
.btn-about{left:172px;top:1419px;width:162px;height:38px}
.headshot{left:663px;top:955px;width:433px;height:558px;background:radial-gradient(ellipse at 50% 35%,#e6c79a 0%,#d9b38a 30%,#eef0f0 62%,#fff 100%);border-radius:0 0 0 40px}
.badge{top:1440px;width:74px;height:73px;background:#1f5e8c;border-radius:6px}
.band{top:1624px;left:0;width:1200px;height:529px;background:var(--teal-soft)}
.section-title{left:0;width:1200px;text-align:center;font-family:"Barlow",sans-serif;font-size:51px;font-weight:400}
.section-title strong{color:var(--teal);font-weight:600}
.testi p{position:absolute;left:27px;right:22px;top:56px;font-size:12.6px;line-height:19.5px;color:#444}
.testi .name{position:absolute;left:25px;top:155px;font-weight:700;font-size:16px;color:var(--ink)}
.testi .stars{position:absolute;left:25px;top:176px;font-size:16px;letter-spacing:4px;color:var(--teal)}
.pager{font-size:12px;font-weight:700;color:#444;display:flex;align-items:center;gap:10px}
.btn-pill{height:35px;font-size:13px}
.blog .thumb{position:absolute;left:26px;top:23px;width:298px;height:203px;border-radius:28px}
.blog .meta{position:absolute;left:28px;top:262px;font-size:11px;color:#555;display:flex;gap:20px;align-items:center}
.blog .meta span{display:flex;align-items:center;gap:6px}
.blog h3{position:absolute;left:28px;top:290px;width:285px;font-family:"Barlow",sans-serif;font-weight:500;font-size:25px;line-height:31px;color:var(--ink)}
.blog .arrow{position:absolute;left:276px;top:364px}
.footer{top:2940px;left:0;width:1200px;height:341px;background:var(--footer)}
.foot-phone{left:178px;top:3018px;display:flex;align-items:center;gap:14px;font-size:22px;font-weight:800;color:var(--white)}
.foot-line{left:186px;display:flex;align-items:flex-start;gap:16px;font-size:14px;line-height:19px;color:var(--white)}
.foot-logo{left:500px;top:2995px;width:224px;height:180px;background:transparent}
.foot-logo .logo-ring{left:10px;top:8px;width:200px;height:164px}
.hours{left:843px;top:3016px;color:var(--white);font-size:13px;line-height:21px}
.hours h4{font-family:"Barlow",sans-serif;color:var(--teal);font-weight:500;font-size:19px;margin-bottom:10px}
.copy{left:0;width:1200px;top:3204px;text-align:center;font-size:11.5px;color:var(--white)}
.social{top:3238px;left:548px;display:flex;gap:26px}
.social i{display:block;width:14px;height:14px;border-radius:50%;background:var(--teal)}
</style>
</head>
<body>

<!-- Header -->
<nav class="nav">
  <a class="active" style="left:178px" href="#">HOME</a>
  <a style="left:254px" href="#">ABOUT</a>
  <a style="left:337px" href="#">SERVICES</a>
  <a style="left:789px" href="#">COACHING</a>
  <a style="left:899px" href="#">BLOG</a>
  <a style="left:970px" href="#">CONTACT</a>
</nav>
<div class="abs call">
  <svg width="22" height="22" viewBox="0 0 24 24" fill="none" stroke="#14a88e" stroke-width="1.6"><path d="M5 3h4l2 5-3 2a12 12 0 0 0 6 6l2-3 5 2v4a2 2 0 0 1-2 2A17 17 0 0 1 3 5a2 2 0 0 1 2-2z"/></svg>
  Call us - <b>+1 555 204 318</b>
</div>
<div class="abs header-line"></div>

<!-- Hero -->
<div class="abs hero-photo" role="img" aria-label="Photo of a coach and a client talking at a table with a tablet"></div>
<div class="abs hero-bg"></div>
<div class="abs logo logo-head"><div class="logo-ring"></div><span style="font-size:23px;margin-top:10px">RISING PATHS</span></div>
<h1 class="abs heading hero-title"><strong>Taking Care</strong>of Your Life Issues!</h1>
<p class="abs hero-text">Get the motivation, guidance, and support you need to get your life on track. You don't need to struggle on your own anymore!</p>
<div class="abs btn btn-hero">SCHEDULE AN APPOINTMENT</div>

<!-- Services -->
<div class="card service" style="left:47px;top:656px;width:348px;height:223px">
  <svg width="348" height="223"><path d="M0,0 C8,20 25,20 45,20 H318 A30,30 0 0 1 348,50 V185 A38,38 0 0 1 310,223 H38 A38,38 0 0 1 0,185 Z" fill="#14a88e"/></svg>
  <h3>Consultancy &amp; Advicing</h3>
  <p>Lorem ipsum dolor sit amet, consectetur adipiscing elit, sed do eiusmod tempor incididunt ut labore et dolore magna aliqua.</p>
  <svg class="arrow" width="46" height="12" fill="none" stroke="#fff" stroke-width="1.5"><path d="M0 6h44M38 1l6 5-6 5"/></svg>
</div>
<div class="card service" style="left:427px;top:656px;width:348px;height:223px">
  <svg width="348" height="223"><path d="M0,0 C8,20 25,20 45,20 H318 A30,30 0 0 1 348,50 V185 A38,38 0 0 1 310,223 H38 A38,38 0 0 1 0,185 Z" fill="#14a88e"/></svg>
  <h3>Problem Solving</h3>
  <p>Lorem ipsum dolor sit amet, consectetur adipiscing elit, sed do eiusmod tempor incididunt ut labore et dolore magna aliqua.</p>
  <svg class="arrow" width="46" height="12" fill="none" stroke="#fff" stroke-width="1.5"><path d="M0 6h44M38 1l6 5-6 5"/></svg>
</div>
<div class="card service" style="left:806px;top:656px;width:348px;height:223px">
  <svg width="348" height="223"><path d="M0,0 C8,20 25,20 45,20 H318 A30,30 0 0 1 348,50 V185 A38,38 0 0 1 310,223 H38 A38,38 0 0 1 0,185 Z" fill="#14a88e"/></svg>
  <h3>Conferencing &amp; Talks</h3>
  <p>Lorem ipsum dolor sit amet, consectetur adipiscing elit, sed do eiusmod tempor incididunt ut labore et dolore magna aliqua.</p>
  <svg class="arrow" width="46" height="12" fill="none" stroke="#fff" stroke-width="1.5"><path d="M0 6h44M38 1l6 5-6 5"/></svg>
</div>

<!-- About -->
<div class="abs headshot" role="img" aria-label="Head shot of the coach"></div>
<svg class="abs" style="left:112px;top:986px" width="596" height="528">
  <defs><linearGradient id="aboutFill" x1="0" y1="0" x2="0" y2="1"><stop offset="0.75" stop-color="#fff"/><stop offset="1" stop-color="#ececec"/></linearGradient></defs>
  <path d="M1,41 A40,40 0 0 1 41,1 H511 A40,40 0 0 1 551,41 V420 C551,470 568,505 594,527 H41 A40,40 0 0 1 1,487 Z" fill="url(#aboutFill)" stroke="#333" stroke-width="1.5"/>
</svg>
<h2 class="abs heading about-title">Rising Paths<strong>Transforms Lives</strong></h2>
<div class="abs about-text">
  <p>Lorem ipsum dolor sit amet, consectetur adipiscing elit, sed do eiusmod tempor incididunt ut labore et dolore magna aliqua. Ut enim ad minim veniam, quis nostrud exercitation ullamco laboris nisi ut aliquip ex ea commodo consequat.</p>
  <p>Duis aute irure dolor in reprehenderit in voluptate velit esse cillum dolore eu fugiat nulla pariatur.</p>
</div>
<div class="abs signature" role="img" aria-label="Handwritten signature"></div>
<div class="abs btn btn-about">ABOUT US</div>
<div class="abs badge" style="left:760px"></div>
<div class="abs badge" style="left:855px;background:#2a5d8a"></div>
<div class="abs badge" style="left:951px;border-radius:50%;background:#2b8cc4"></div>

<!-- Testimonials -->
<div class="abs band"></div>
<h2 class="abs section-title" style="top:1690px"><strong>Client's</strong> Testimonials</h2>

<div class="card testi" style="left:47px;top:1784px;width:256px;height:230px">
  <svg width="256" height="230"><path d="M1,1 C8,22 22,26 40,26 H225 A30,30 0 0 1 255,56 V199 A30,30 0 0 1 225,229 H31 A30,30 0 0 1 1,199 Z" fill="#fff" stroke="#14a88e" stroke-width="1.5"/></svg>
  <p>Lorem ipsum dolor sit amet, consectetur adipiscing elit, sed do eiusmod tempor incididunt ut labore et dolore magna aliqua.</p>
  <div class="name">Lena Marsh</div><div class="stars">★★★★★</div>
</div>
<div class="card testi" style="left:331px;top:1784px;width:256px;height:230px">
  <svg width="256" height="230"><path d="M1,1 C8,22 22,26 40,26 H225 A30,30 0 0 1 255,56 V199 A30,30 0 0 1 225,229 H31 A30,30 0 0 1 1,199 Z" fill="#fff" stroke="#14a88e" stroke-width="1.5"/></svg>
  <p>Lorem ipsum dolor sit amet, consectetur adipiscing elit, sed do eiusmod tempor incididunt ut labore et dolore magna aliqua.</p>
  <div class="name">Lena Marsh</div><div class="stars">★★★★★</div>
</div>
<div class="card testi" style="left:615px;top:1784px;width:256px;height:230px">
  <svg width="256" height="230"><path d="M1,1 C8,22 22,26 40,26 H225 A30,30 0 0 1 255,56 V199 A30,30 0 0 1 225,229 H31 A30,30 0 0 1 1,199 Z" fill="#fff" stroke="#14a88e" stroke-width="1.5"/></svg>
  <p>Lorem ipsum dolor sit amet, consectetur adipiscing elit, sed do eiusmod tempor incididunt ut labore et dolore magna aliqua.</p>
  <div class="name">Lena Marsh</div><div class="stars">★★★★★</div>
</div>
<div class="card testi" style="left:899px;top:1784px;width:256px;height:230px">
  <svg width="256" height="230"><path d="M1,1 C8,22 22,26 40,26 H225 A30,30 0 0 1 255,56 V199 A30,30 0 0 1 225,229 H31 A30,30 0 0 1 1,199 Z" fill="#fff" stroke="#14a88e" stroke-width="1.5"/></svg>
  <p>Lorem ipsum dolor sit amet, consectetur adipiscing elit, sed do eiusmod tempor incididunt ut labore et dolore magna aliqua.</p>
  <div class="name">Lena Marsh</div><div class="stars">★★★★★</div>
</div>

<div class="abs pager" style="left:397px;top:2072px"><svg width="32" height="10" fill="none" stroke="#333" stroke-width="1.2"><path d="M32 5H1M6 1L1 5l5 4"/></svg>PREV</div>
<div class="abs btn btn-pill" style="left:508px;top:2061px;width:182px">ALL TESTIMONIALS</div>
<div class="abs pager" style="left:726px;top:2072px">NEXT<svg width="32" height="10" fill="none" stroke="#333" stroke-width="1.2"><path d="M0 5h31M26 1l5 4-5 4"/></svg></div>

<!-- Blogs -->
<h2 class="abs section-title" style="top:2215px">Latest <strong>Blogs</strong></h2>

<div class="card blog" style="left:47px;top:2319px;width:350px;height:454px">
  <svg width="350" height="454"><path d="M1,452 V36 A35,35 0 0 1 36,1 H312 A35,35 0 0 1 347,36 V370 A35,35 0 0 1 312,405 H62 C32,405 12,428 1,452 Z" fill="#fff" stroke="#333" stroke-width="1.5"/></svg>
  <div class="thumb" role="img" aria-label="Photo of a man leaning back at his desk" style="background:linear-gradient(160deg,#eae6df,#c98a3e 60%,#7a5a3b)"></div>
  <div class="meta"><span>▢ JANUARY 12, 2018</span><span>◯ BY CLARA</span></div>
  <h3>Thoughts on Procrastination</h3>
  <svg class="arrow" width="46" height="12" fill="none" stroke="#14a88e" stroke-width="1.8"><path d="M0 6h44M38 1l6 5-6 5"/></svg>
</div>
<div class="card blog" style="left:425px;top:2319px;width:350px;height:454px">
  <svg width="350" height="454"><path d="M1,452 V36 A35,35 0 0 1 36,1 H312 A35,35 0 0 1 347,36 V370 A35,35 0 0 1 312,405 H62 C32,405 12,428 1,452 Z" fill="#fff" stroke="#333" stroke-width="1.5"/></svg>
  <div class="thumb" role="img" aria-label="Photo of a team of cafe workers" style="background:linear-gradient(160deg,#5b4a40,#d8d4cf 45%,#6b5346)"></div>
  <div class="meta"><span>▢ JANUARY 12, 2018</span><span>◯ BY CLARA</span></div>
  <h3>People who made inspiring life changes</h3>
  <svg class="arrow" width="46" height="12" fill="none" stroke="#14a88e" stroke-width="1.8"><path d="M0 6h44M38 1l6 5-6 5"/></svg>
</div>
<div class="card blog" style="left:803px;top:2319px;width:350px;height:454px">
  <svg width="350" height="454"><path d="M1,452 V36 A35,35 0 0 1 36,1 H312 A35,35 0 0 1 347,36 V370 A35,35 0 0 1 312,405 H62 C32,405 12,428 1,452 Z" fill="#fff" stroke="#333" stroke-width="1.5"/></svg>
  <div class="thumb" role="img" aria-label="Photo of two people walking through a green field" style="background:linear-gradient(180deg,#c9c49a,#7f9a5a 45%,#3f7a2c)"></div>
  <div class="meta"><span>▢ JANUARY 12, 2018</span><span>◯ BY CLARA</span></div>
  <h3>The incredible power of small changes</h3>
  <svg class="arrow" width="46" height="12" fill="none" stroke="#14a88e" stroke-width="1.8"><path d="M0 6h44M38 1l6 5-6 5"/></svg>
</div>

<div class="abs pager" style="left:422px;top:2841px"><svg width="32" height="10" fill="none" stroke="#333" stroke-width="1.2"><path d="M32 5H1M6 1L1 5l5 4"/></svg>PREV</div>
<div class="abs btn btn-pill" style="left:532px;top:2829px;width:134px">ALL BLOGS</div>
<div class="abs pager" style="left:701px;top:2841px">NEXT<svg width="32" height="10" fill="none" stroke="#333" stroke-width="1.2"><path d="M0 5h31M26 1l5 4-5 4"/></svg></div>

<!-- Footer -->
<footer class="abs footer"></footer>
<div class="abs foot-phone">
  <svg width="30" height="30" viewBox="0 0 24 24" fill="none" stroke="#14a88e" stroke-width="1.5"><path d="M5 3h4l2 5-3 2a12 12 0 0 0 6 6l2-3 5 2v4a2 2 0 0 1-2 2A17 17 0 0 1 3 5a2 2 0 0 1 2-2z"/></svg>
  +1 555 204 318
</div>
<div class="abs foot-line" style="top:3068px">
  <svg width="16" height="18" viewBox="0 0 16 20" fill="#14a88e"><path d="M8 0a7 7 0 0 0-7 7c0 5 7 13 7 13s7-8 7-13a7 7 0 0 0-7-7zm0 10a3 3 0 1 1 0-6 3 3 0 0 1 0 6z"/></svg>
  <span>48 Orchard Lane.<br>United States. 10482</span>
</div>
<div class="abs foot-line" style="top:3112px">
  <svg width="16" height="12" viewBox="0 0 16 12" fill="none" stroke="#14a88e" stroke-width="1.2"><rect x=".6" y=".6" width="14.8" height="10.8"/><path d="M1 1l7 6 7-6"/></svg>
  <span>info@risingpaths.com</span>
</div>
<div class="abs logo foot-logo"><div class="logo-ring"></div><span style="font-size:24px;color:#fff">RISING PATHS</span></div>
<div class="abs hours">
  <h4>OFFICE HOURS</h4>
  Mon - Wed : 8am - 7pm<br>Thursday : 8am - 5pm<br>Friday : 8am - 6pm<br>Sat - Sun : Closed
</div>
<p class="abs copy">Copyright © <b>Rising Paths</b> 2022. All Right Reserved</p>
<div class="abs social"><i></i><i></i><i></i></div>

</body>
</html>
```